Fresh web design for high profile Golf Club

We need an exciting web site that serves both members and visitors. Our current site has the relevant sections and pages but lacks a visual impact. There are a number of very good looking golf websites out there and we want to look the best.
We need a site that will attract golfers from all over Australia to come to our course to enjoy one of the finest 36 hole championship courses as well as fantastic clubhouse facilities on their next golfing holiday.
The member section needs to provide relevant information pages and regular news and event updates to 3000 members. We are situated on the Corran River with over 300 days of sunshine and ideal golfing weather every year.
We would like to stay with our existing logo and colours as a theme.

Target Market(s)

Golfers looking for golf holiday packages.

Industry/Entity Type

Club

Requirements
Must have
• Must have contact number for golf package holidays. Must have button for member entry and button for visitor entry. Existing site is www.brelharbourgolf.com.au. Looking for a big improvement in the look of the home page.
Nice to have
• Would like constantly updated weather reporting from source such as weather channel.

```html
<!DOCTYPE html>
<html lang="en">
<head>
<meta charset="utf-8">
<title>Brel Harbour Golf Club</title>
<link rel="stylesheet" href="https://fonts.googleapis.com/css2?family=Arimo:wght@400;700&family=Cinzel:wght@400;700&family=Lora:ital@1&display=swap">
<style>
:root{
  --teal:#2a8588;
  --teal-band:#5f999b;
  --teal-box:#6ea4a6;
  --teal-box-dark:#5b9193;
  --green:#8cb33e;
  --green-dark:#7aa032;
  --text:#555;
  --dark:#333;
  --grey-box:#4a4a4a;
  --light-box:#efefef;
  --line:#dcdcdc;
  --link:#2a6f9a;
  --white:#fff;
}
*{margin:0;padding:0;box-sizing:border-box}
html,body{width:1126px;height:1200px;overflow:hidden}
body{position:relative;background:var(--white);font-family:"Arimo",Arial,sans-serif;color:var(--text)}
.abs{position:absolute}
.top-band{left:0;top:96px;width:1126px;height:214px;background:linear-gradient(#fff 0%,#b7d1d2 40%,var(--teal-band) 100%)}
.logo{left:33px;top:20px;display:flex;align-items:center;gap:12px}
.logo-dot{width:58px;height:58px;border-radius:50%;background:var(--teal-box)}
.logo-name{font-size:20px;letter-spacing:3px;color:#444;line-height:26px;font-weight:400}
.nav{left:339px;top:40px;display:flex;font-size:12px;color:#555}
.nav span{padding:0 11px;border-left:1px solid #bbb;line-height:13px}
.nav span:first-child{border-left:none;padding-left:0;color:var(--green)}
.nav span:last-child{padding-right:0}
.member-tab{left:742px;top:79px;width:268px;height:25px;background:var(--green);border-radius:4px 4px 0 0;border:1px solid var(--green-dark);color:#fff;font-size:12px;display:flex;align-items:center;justify-content:center;gap:10px}
.hero-frame{left:107px;top:107px;width:907px;height:339px;background:#fff;box-shadow:0 0 8px rgba(0,0,0,.15)}
.hero-photo{left:115px;top:113px;width:890px;height:325px;background:linear-gradient(160deg,#e8eef0 0%,#b9c9a0 30%,#6f9a3a 60%,#3f6b1e 100%)}
.hero-caption{left:531px;top:232px;font-family:"Cinzel",serif;font-size:20px;color:#fff;text-shadow:0 1px 3px rgba(0,0,0,.5)}
.slider-dots{left:936px;top:410px;display:flex;gap:5px}
.slider-dots i{width:14px;height:14px;border-radius:50%;background:#555;border:1px solid #888}
.main-panel{left:88px;top:456px;width:948px;height:694px;background:#fff;box-shadow:0 0 10px rgba(0,0,0,.12)}
.heading{color:var(--teal);font-size:15px;font-weight:400}
.heading small{font-size:12px;color:var(--teal)}
.body-copy{left:133px;width:566px;font-size:12px;line-height:16.5px;color:var(--text)}
.divider{left:130px;width:583px;height:1px;background:var(--line)}
.photo-frame{border:1px solid #ccc;padding:5px;background:#fff;box-shadow:0 1px 3px rgba(0,0,0,.15)}
.photo-frame div{width:100%;height:100%}
.news-title{left:349px;top:845px;font-size:12px;font-weight:700;color:var(--dark)}
.news-meta{left:349px;top:863px;font-family:"Lora",serif;font-style:italic;font-size:11px;color:#999}
.news-copy{left:349px;top:884px;width:362px;font-size:12px;line-height:16.5px}
.side-box{left:752px;width:253px;border-radius:3px;box-shadow:0 1px 4px rgba(0,0,0,.25)}
.weather{top:476px;height:148px;background:var(--grey-box);color:#fff;text-align:center}
.weather h3{font-size:13px;font-weight:700;margin-top:15px}
.weather-days{display:flex;justify-content:space-around;margin-top:12px}
.weather-day{width:80px;font-size:12px;line-height:15px}
.weather-day+.weather-day{border-left:1px solid #666}
.weather-day svg{display:block;margin:0 auto 4px}
.offer{top:634px;height:134px;background:linear-gradient(var(--teal-box),var(--teal-box-dark));color:#fff;text-align:center}
.offer h3{font-family:"Cinzel",serif;font-size:24px;font-weight:400;margin-top:16px;line-height:28px}
.offer p{font-style:italic;font-size:12px;border-top:1px solid rgba(255,255,255,.5);margin:4px 15px 0;padding-top:4px}
.offer strong{display:block;font-size:40px;font-weight:400;margin-top:6px}
.members{top:781px;height:128px;background:var(--light-box)}
.members h3{background:var(--green);color:#fff;font-size:13px;font-weight:700;height:38px;line-height:38px;padding-left:15px;border-radius:3px 3px 0 0}
.members p{font-size:12px;line-height:16.5px;padding:9px 12px;width:236px;color:#555}
.download{height:59px;background:var(--light-box);display:flex;align-items:center;padding-left:20px;gap:12px;font-size:11px;line-height:12.5px;color:#444}
.download-icon{width:34px;height:36px;background:#b81818;border-radius:3px;flex:none}
.download a{color:var(--link);text-decoration:none}
.updates{top:1068px;height:77px;background:linear-gradient(var(--teal-box),var(--teal-box-dark));color:#fff}
.updates h3{font-size:13px;font-weight:700;padding:11px 0 0 15px}
.social{display:flex;gap:18px;padding:9px 0 0 15px}
.social i{width:36px;height:36px;border-radius:5px;display:flex;align-items:center;justify-content:center}
.footer{left:0;top:1175px;width:1126px;height:25px;background:var(--teal-box);color:#fff;font-size:11px;display:flex;justify-content:center;align-items:center;gap:12px}
</style>
</head>
<body>
<div class="abs top-band"></div>

<div class="abs logo">
  <div class="logo-dot"></div>
  <div class="logo-name">BREL HARBOUR<br>GOLF CLUB</div>
</div>

<nav class="abs nav">
  <span>Home</span><span>Membership</span><span>Golf</span><span>Club House</span><span>News &amp; Events</span><span>Packages</span><span>Brel Harbour</span><span>Gallery</span><span>Contact</span>
</nav>

<div class="abs member-tab"><span>CLUB MEMEBERS LOGIN</span><span>|</span><span>JOIN NOW</span></div>

<div class="abs hero-frame"></div>
<div class="abs hero-photo" role="img" aria-label="Gloved hand placing a golf ball on a red tee beside an iron club on a sunlit fairway"></div>
<div class="abs hero-caption">A great golf course is just the beginning...</div>
<div class="abs slider-dots"><i></i><i></i><i></i></div>

<div class="abs main-panel"></div>

<h2 class="abs heading" style="left:133px;top:473px">"A great golf course is just the beginning..."</h2>
<p class="abs body-copy" style="top:506px">There's so much to do on the beautiful Corran River. Discover Brel Harbour's 36 Hole Championship Golf Course, glorious golden sandy beaches, Harbour Sport Aviation aerodrome, the Historic Air Museum, walking tracks, State Forests, National Parks and so much more. Experience the history, charm and natural assets of this beautiful Corran River town only 3 hours drive from Melbourne at the start of the Kessing Highway.</p>
<p class="abs body-copy" style="top:605px">The climate is better than Australia's famous Gold Coast with more than 300 days of sunshine, and mean temperatures of around 28°Celsius in January and 15°Celsius in July. Brel Harbour Golf Club invites you to experience this exceptional sporting venue situated on Australia's mighty Corran River. Home of the Southern Pro Trainee Championships this is one of Australia's best presented 36 Hole Championship Golf Courses. If you're chasing that elusive Murray Cod, Waterskiing, Boating, Fishing, relaxing on a houseboat or sunbaking on our golden beaches, Brel Harbour is the perfect place to base yourself for a Corran River break. We are central to all the Corran attractions as well as having over 350 golf holes within an hours drive. Social golfers are welcome here 7 days a week. A great golf course is just the beginning...</p>

<div class="abs divider" style="top:779px"></div>
<h2 class="abs heading" style="left:133px;top:802px">Latest News &amp; Events <small>/ view more</small></h2>
<div class="abs photo-frame" style="left:130px;top:843px;width:198px;height:110px"><div role="img" aria-label="Group of golfers chatting on the course" style="background:linear-gradient(#cfe6f2,#9fc97a 60%,#5f8f36)"></div></div>
<div class="abs news-title">Charity Golf Cup</div>
<div class="abs news-meta">November 1 2012, 8 Comments</div>
<p class="abs news-copy">Lorem ipsum dolor sit amet, consectetuer adipiscing elit, sed diam nonummy nibh euismod tincidunt ut laoreet dolore magna aliquam erat volutpat. Ut wisi enim ad minim veniam, quis nostrud exerci tation ullamcorper suscipit lobortis nisl ut aliquip ex ea minim.</p>

<div class="abs divider" style="top:975px"></div>
<h2 class="abs heading" style="left:133px;top:1000px">Gallery - Golfing Greens, Clubhouse &amp; Events</h2>
<div class="abs photo-frame" style="left:130px;top:1043px;width:187px;height:104px"><div role="img" aria-label="Golfer following through a swing" style="background:linear-gradient(#7fb6e0,#3a79c0 70%,#2d5f9a)"></div></div>
<div class="abs photo-frame" style="left:326px;top:1043px;width:187px;height:104px"><div role="img" aria-label="Aerial view of fairways beside a lake" style="background:linear-gradient(#bcd6c8,#5d8f4a 40%,#4d7d3a)"></div></div>
<div class="abs photo-frame" style="left:519px;top:1043px;width:187px;height:104px"><div role="img" aria-label="Gloved hand holding a golf ball over grass" style="background:linear-gradient(#dfe6de,#a8c582 50%,#5d8e2e)"></div></div>

<section class="abs side-box weather">
  <h3>BREL HARBOUR - WEATHER REPORT</h3>
  <div class="weather-days">
    <div class="weather-day">
      <svg width="50" height="34" viewBox="0 0 50 34"><circle cx="31" cy="13" r="9" fill="#f3b324"/><path d="M10 30h30a8 8 0 0 0 0-16 11 11 0 0 0-21 2 7 7 0 0 0-9 14z" fill="#eee" stroke="#222" stroke-width="2"/></svg>
      Saturday<br>14 | 25
    </div>
    <div class="weather-day">
      <svg width="50" height="34" viewBox="0 0 50 34"><circle cx="25" cy="17" r="14" fill="#f7c21e" stroke="#222" stroke-width="2"/><circle cx="25" cy="17" r="9" fill="#f39a14"/></svg>
      Sunday<br>16 | 27
    </div>
    <div class="weather-day">
      <svg width="50" height="34" viewBox="0 0 50 34"><circle cx="31" cy="13" r="9" fill="#f3b324"/><path d="M10 30h30a8 8 0 0 0 0-16 11 11 0 0 0-21 2 7 7 0 0 0-9 14z" fill="#eee" stroke="#222" stroke-width="2"/></svg>
      Monday<br>14 | 26
    </div>
  </div>
</section>

<section class="abs side-box offer">
  <h3>SPECIAL OFFER</h3>
  <p>On ALL Our Packages this Summer!</p>
  <strong>10% OFF</strong>
</section>

<section class="abs side-box members">
  <h3>CLUB MEMEBERS</h3>
  <p>Our annual dinner meeting will be held on the 23 November 2012 at the Club House. Please RSVP by the 15th November 2012 to book your seat.</p>
</section>

<div class="abs side-box download" style="top:922px">
  <div class="download-icon"></div>
  <div>THE BREL HARBOUR GOLF CLUB<br>2012 ANNUAL REPORT<br><a href="#">Download the PDF HERE</a></div>
</div>
<div class="abs side-box download" style="top:995px">
  <div class="download-icon"></div>
  <div>THE BREL HARBOUR GOLF CLUB<br>2012 NOTICE OF AGM<br><a href="#">Download the PDF HERE</a></div>
</div>

<section class="abs side-box updates">
  <h3>GET THE LATEST UPDATES</h3>
  <div class="social">
    <i style="background:#3b5ea0"></i>
    <i style="background:#38a9dc"></i>
    <i style="background:#f08a1c"><svg width="22" height="22" viewBox="0 0 22 22"><circle cx="4" cy="18" r="3" fill="#fff"/><path d="M2 9a11 11 0 0 1 11 11M2 2a18 18 0 0 1 18 18" stroke="#fff" stroke-width="3" fill="none"/></svg></i>
    <i style="background:#6da82c"><svg width="24" height="18" viewBox="0 0 24 18"><rect x="1" y="1" width="22" height="16" fill="none" stroke="#fff" stroke-width="2"/><path d="M1 1l11 9 11-9" stroke="#fff" stroke-width="2" fill="none"/></svg></i>
  </div>
</section>

<footer class="abs footer">
  <span>Brel Harbour Golf Club</span><span>|</span><span>Lindell Rd, Brel Harbour N.S.W. 2790</span><span>|</span><span>Contact 1800 555 014</span><span>|</span><span>Copyright © Brel Harbour Golf Club 2012 All Rights Reserved</span><span>|</span><span>Private Policy</span>
</footer>
</body>
</html>
```